Business Card for Consulting Company

I would need a business card for my consulting company - the company brand and logos are defined and shared as part of this project. The proposed design for the business card can be reused as inspiration for my email signature.

```html
<!DOCTYPE html>
<html lang="en">
<head>
<meta charset="utf-8">
<title>Halden Partners – Business Card</title>
<link href="https://fonts.googleapis.com/css2?family=Open+Sans:wght@400;700&display=swap" rel="stylesheet">
<style>
  :root {
    --teal: #1fa8a6;
    --ink: #2b2b2b;
    --muted: #555555;
    --paper: #fbfbfa;
    --night: #1d1d1d;
    --stage: #e9e6e1;
  }
  * { margin: 0; padding: 0; box-sizing: border-box; }
  html, body {
    width: 1200px;
    height: 1023px;
    overflow: hidden;
    background: var(--stage);
    font-family: "Open Sans", Arial, sans-serif;
  }
  .canvas {
    position: relative;
    width: 1200px;
    height: 1023px;
  }
  .card {
    position: absolute;
    width: 540px;
    height: 340px;
    border-radius: 3px;
    box-shadow: 0 10px 30px rgba(0, 0, 0, 0.18);
  }
  .card--front {
    left: 70px;
    top: 170px;
    background: var(--paper);
  }
  .card--back {
    left: 590px;
    top: 520px;
    background: var(--night);
  }
  .brand {
    position: absolute;
    display: flex;
    align-items: center;
    gap: 10px;
    font-weight: 700;
    color: var(--teal);
    white-space: nowrap;
  }
  .brand__dot {
    border-radius: 50%;
    background: var(--teal);
  }
  .card--front .brand {
    right: 34px;
    top: 38px;
    font-size: 22px;
  }
  .card--front .brand__dot { width: 14px; height: 14px; }
  .card--back .brand {
    left: 50%;
    top: 50%;
    transform: translate(-50%, -50%);
    font-size: 34px;
  }
  .card--back .brand__dot { width: 20px; height: 20px; }
  .holder {
    position: absolute;
    left: 44px;
    bottom: 40px;
    width: 300px;
  }
  .holder__name {
    font-size: 26px;
    font-weight: 700;
    color: var(--teal);
    line-height: 1.1;
  }
  .holder__role {
    font-size: 15px;
    color: var(--ink);
    margin-top: 4px;
  }
  .holder__rule {
    border: 0;
    border-top: 1.5px solid var(--teal);
    width: 280px;
    margin: 10px 0 14px;
  }
  .contact {
    list-style: none;
    font-size: 12.5px;
    color: var(--muted);
    line-height: 1.75;
  }
  .contact__web { color: var(--teal); }
</style>
</head>
<body>
  <main class="canvas">
    <section class="card card--front" aria-label="Business card front">
      <div class="brand"><span class="brand__dot"></span>Halden Partners</div>
      <div class="holder">
        <h1 class="holder__name">Marin Aubert</h1>
        <p class="holder__role">Founder &amp; CEO</p>
        <hr class="holder__rule">
        <ul class="contact">
          <li>P : +41 79 000 4821</li>
          <li>M : marin.a@haldenpartners.ch</li>
          <li>W : <span class="contact__web">www.haldenpartners.ch</span></li>
        </ul>
      </div>
    </section>
    <section class="card card--back" aria-label="Business card back">
      <div class="brand"><span class="brand__dot"></span>Halden Partners</div>
    </section>
  </main>
</body>
</html>
```